Barrister at Law needs Business Card Design

Need a business card design for Barrister at Law. Double sided. Simple Miles Tordoff and Barrister at Law on one side with contact details on the other side. I would like a professional design using Black or Platinum. Details on reverse side would include qualifications - Bcom-Llb and Acc Spec Commercial Litigation. I have attached the logo. Contact details would include address/ Po Box/ Phone/Fax/Mobile/email. I would like to use raised print or spot gloss.

```html
<!DOCTYPE html>
<html lang="en">
<head>
<meta charset="utf-8">
<title>Miles Tordoff – Barrister-at-Law Business Card</title>
<link rel="stylesheet" href="https://fonts.googleapis.com/css2?family=Cinzel:wght@500&family=Open+Sans:wght@400;600&display=swap">
<style>
  :root {
    --backdrop: #3a3330;
    --card-black: #141414;
    --card-edge: #202020;
    --silver-light: #f2f2f2;
    --silver-dark: #8e8e8e;
    --ink-light: #e6e6e6;
    --accent-blue: #2a7fc4;
    --accent-blue-dark: #1b5f99;
    --gloss: #2c2c2c;
  }
  html, body {
    margin: 0;
    padding: 0;
    width: 1200px;
    height: 814px;
    overflow: hidden;
    background: var(--backdrop);
  }
  .sheet {
    width: 1200px;
    height: 814px;
    display: flex;
    align-items: center;
    justify-content: center;
    gap: 40px;
  }
  .card {
    position: relative;
    width: 520px;
    height: 297px;
    background: var(--card-black);
    border-radius: 3px;
    box-shadow: 0 14px 30px rgba(0,0,0,0.45);
    overflow: hidden;
  }
  /* front */
  .card-front .identity {
    position: absolute;
    left: 66px;
    top: 78px;
    font-family: 'Cinzel', serif;
    font-weight: 500;
    text-transform: uppercase;
  }
  .card-front .name {
    font-size: 30px;
    letter-spacing: 1px;
    background: linear-gradient(180deg, var(--silver-light) 0%, var(--silver-dark) 100%);
    -webkit-background-clip: text;
    background-clip: text;
    color: transparent;
    margin: 0;
  }
  .card-front .title {
    font-size: 19px;
    letter-spacing: 0.5px;
    color: var(--silver-dark);
    margin: 4px 0 0 4px;
  }
  /* back */
  .card-back .brand {
    position: absolute;
    left: 40px;
    top: 44px;
    display: flex;
    align-items: center;
    gap: 10px;
    font-family: 'Open Sans', sans-serif;
    font-weight: 600;
    font-size: 22px;
    color: var(--ink-light);
  }
  .card-back .brand-square {
    width: 22px;
    height: 22px;
    background: var(--accent-blue);
  }
  .card-back .stripe {
    position: absolute;
    left: 0;
    bottom: 0;
    width: 520px;
    height: 100px;
  }
  .card-back .contact {
    position: absolute;
    right: 24px;
    top: 120px;
    font-family: 'Open Sans', sans-serif;
    font-size: 12.5px;
    line-height: 19px;
    color: var(--ink-light);
    text-align: right;
    list-style: none;
    margin: 0;
    padding: 0;
  }
  .card-back .contact li {
    display: flex;
    justify-content: flex-end;
    align-items: center;
    gap: 8px;
  }
  .card-back .contact svg {
    width: 12px;
    height: 12px;
    fill: var(--accent-blue);
  }
  .card-back .contact .no-icon { padding-right: 20px; }
  .card-back .website {
    position: absolute;
    right: 44px;
    bottom: 12px;
    font-family: 'Open Sans', sans-serif;
    font-size: 14px;
    letter-spacing: 2px;
    color: #ffffff;
  }
</style>
</head>
<body>
<main class="sheet">
  <section class="card card-front">
    <div class="identity">
      <h1 class="name">Miles Tordoff</h1>
      <p class="title">Barrister-at-Law</p>
    </div>
  </section>

  <section class="card card-back">
    <div class="brand"><span class="brand-square"></span>Tordoff</div>

    <svg class="stripe" viewBox="0 0 520 100" preserveAspectRatio="none" aria-hidden="true">
      <defs>
        <linearGradient id="glossBand" x1="0" y1="0" x2="1" y2="0">
          <stop offset="0" stop-color="#1a1a1a"/>
          <stop offset="0.45" stop-color="#5a5a5a"/>
          <stop offset="0.6" stop-color="#222"/>
          <stop offset="1" stop-color="#161616"/>
        </linearGradient>
      </defs>
      <polygon points="0,18 520,58 520,62 0,24" fill="var(--accent-blue)"/>
      <polygon points="0,24 520,62 520,66 260,64 0,46" fill="url(#glossBand)"/>
      <polygon points="260,64 520,66 520,100 240,100 0,100 0,92 230,92" fill="var(--accent-blue)"/>
      <polygon points="0,92 230,92 0,100" fill="var(--accent-blue-dark)"/>
    </svg>

    <ul class="contact">
      <li class="no-icon">2140 Larkspur Court</li>
      <li class="no-icon">Juneau, Alaska 99801</li>
      <li>907 312 4480
        <svg viewBox="0 0 24 24"><path d="M6.6 10.8a15.1 15.1 0 0 0 6.6 6.6l2.2-2.2a1 1 0 0 1 1-.25 11.4 11.4 0 0 0 3.6.57 1 1 0 0 1 1 1V20a1 1 0 0 1-1 1A17 17 0 0 1 3 4a1 1 0 0 1 1-1h3.5a1 1 0 0 1 1 1c0 1.25.2 2.45.57 3.57a1 1 0 0 1-.25 1z"/></svg>
      </li>
      <li>907 918 2256
        <svg viewBox="0 0 24 24"><path d="M7 1h10a2 2 0 0 1 2 2v18a2 2 0 0 1-2 2H7a2 2 0 0 1-2-2V3a2 2 0 0 1 2-2zm0 3v14h10V4zm5 15.2a1.1 1.1 0 1 0 0 2.2 1.1 1.1 0 0 0 0-2.2z"/></svg>
      </li>
      <li>907 312 4481
        <svg viewBox="0 0 24 24"><path d="M6 2h9l3 3v4H6zm-2 8h16a2 2 0 0 1 2 2v8H2v-8a2 2 0 0 1 2-2zm3 4v2h4v-2z"/></svg>
      </li>
      <li>miles@tordofflaw.com
        <svg viewBox="0 0 24 24"><path d="M2 5h20v14H2zm2 2v.5l8 5 8-5V7zm0 2.8V17h16V9.8l-8 5z"/></svg>
      </li>
    </ul>

    <div class="website">www.tordofflaw.com</div>
  </section>
</main>
</body>
</html>
```